Dribblecake Bites
2 x business cards, letter head, with complements and envelopes
Dribblecake Bites - Food
Creative Brief
Bright & Fun-filled
Percy Lantern
Managing Director
NA
Percy.Lantern@dribblecakebites.com.au
www.dribblecakebites.com.au
card 2 Teodor Blum Business Manager 0417583926 Teodorblum@quillnet.com www.dribblecakebites.com.au
logo ect

```html
<!DOCTYPE html>
<html lang="en">
<head>
<meta charset="utf-8">
<title>Dribblecake Bites Stationery</title>
<link href="https://fonts.googleapis.com/css2?family=Fredoka:wght@600&family=Open+Sans:wght@400;600&display=swap" rel="stylesheet">
<style>
:root{
  --bg-light:#5e5e5e;
  --bg-dark:#2b2b2b;
  --paper:#ffffff;
  --brown:#5a2712;
  --orange:#c8611f;
  --ink:#4a3a32;
  --rule:#dedede;
}
*{margin:0;padding:0;box-sizing:border-box}
html,body{width:1200px;height:389px;overflow:hidden}
body{
  position:relative;
  background:radial-gradient(ellipse at 50% 40%,var(--bg-light),var(--bg-dark));
  font-family:"Open Sans",sans-serif;
  color:var(--ink);
}
.piece{position:absolute;background:var(--paper);overflow:hidden;box-shadow:0 2px 6px rgba(0,0,0,.45)}
.piece > svg.trim{position:absolute;left:0;top:0}
.brand{font-family:"Fredoka",sans-serif;font-weight:600;color:var(--brown);white-space:nowrap;line-height:1}
.mascot-area{position:absolute;border-radius:50%;background:radial-gradient(circle,rgba(90,39,18,.10),rgba(90,39,18,0) 70%)}
.tiny{font-size:4px;line-height:1.55;white-space:nowrap}
.strong{font-weight:600;color:var(--brown)}

/* business cards */
.card{width:153px;height:85px}
.card-percy{left:10px;top:158px}
.card-teodor{left:175px;top:158px}
.card-back-light{left:10px;top:264px}
.card-back-dark{left:175px;top:264px;background:var(--brown)}
.card .brand{position:absolute;left:10px;top:12px;font-size:12px}
.card .contact{position:absolute;left:10px;top:46px}
.card .contact .name{font-size:5px}
.card .details{position:absolute;right:8px;top:48px;text-align:right}
.card-back-light .brand,.card-back-dark .brand{left:0;right:0;text-align:center;font-size:14px}
.card-back-light .brand{top:34px}
.card-back-dark .brand{top:60px;color:var(--paper)}
.card-back-dark .mascot-area{left:46px;top:4px;width:60px;height:60px;background:radial-gradient(circle,rgba(200,97,31,.6),rgba(90,39,18,0) 70%)}

/* letterheads */
.letterhead{width:254px;height:341px;top:24px}
.letterhead-one{left:336px}
.letterhead-two{left:605px}
.letterhead .brand{position:absolute;top:18px;font-size:13px}
.letterhead-one .brand{left:18px}
.letterhead-two .brand{left:0;right:0;text-align:center}
.letterhead .head-info{position:absolute;left:146px;top:19px}
.letterhead .mascot-area{left:52px;top:110px;width:150px;height:150px}
.letterhead .footer{position:absolute;left:0;right:0;bottom:8px;text-align:center}

/* envelope */
.envelope{left:873px;top:144px;width:318px;height:78px}
.envelope .brand{position:absolute;left:0;right:0;top:10px;text-align:center;font-size:12px}
.envelope .web{position:absolute;left:0;right:0;top:26px;text-align:center}

/* compliments slip */
.compliments{left:860px;top:230px;width:331px;height:120px}
.compliments .brand{position:absolute;left:14px;top:14px;font-size:14px}
.compliments .note{position:absolute;right:18px;top:17px;font-size:7px}
.compliments .footer{position:absolute;right:18px;bottom:18px}
</style>
</head>
<body>

<section class="piece card card-percy">
  <svg class="trim" width="153" height="85" viewBox="0 0 153 85"><path d="M0 62 Q8 80 48 85 L0 85 Z" fill="var(--brown)"/></svg>
  <div class="brand">Dribblecake Bites</div>
  <div class="contact tiny"><div class="name strong">Percy Lantern</div>Managing Director</div>
  <div class="details tiny">Percy.Lantern@dribblecakebites.com.au<br>www.dribblecakebites.com.au</div>
</section>

<section class="piece card card-teodor">
  <svg class="trim" width="153" height="85" viewBox="0 0 153 85"><path d="M0 62 Q8 80 48 85 L0 85 Z" fill="var(--brown)"/></svg>
  <div class="brand">Dribblecake Bites</div>
  <div class="contact tiny"><div class="name strong">Teodor Blum</div>Business Manager</div>
  <div class="details tiny">0417583926<br>Teodorblum@quillnet.com<br>www.dribblecakebites.com.au</div>
</section>

<section class="piece card card-back-light">
  <svg class="trim" width="153" height="85" viewBox="0 0 153 85"><path d="M0 62 Q8 80 48 85 L0 85 Z" fill="var(--brown)"/></svg>
  <div class="brand">Dribblecake Bites</div>
</section>

<section class="piece card card-back-dark">
  <div class="mascot-area" role="img" aria-label="Smiling dribblecake mascot illustration"></div>
  <div class="brand">Dribblecake Bites</div>
</section>

<section class="piece letterhead letterhead-one">
  <svg class="trim" width="254" height="341" viewBox="0 0 254 341">
    <path d="M214 0 Q246 6 254 36 L254 0 Z" fill="var(--brown)"/>
    <path d="M0 296 Q6 334 42 341 L0 341 Z" fill="var(--brown)"/>
  </svg>
  <div class="brand">Dribblecake Bites</div>
  <div class="head-info tiny">PO Box 14 Sweetvale NSW 2000<br>Percy.Lantern@dribblecakebites.com.au</div>
  <div class="mascot-area" role="img" aria-label="Faint dribblecake mascot illustration"></div>
  <div class="footer tiny">www.dribblecakebites.com.au</div>
</section>

<section class="piece letterhead letterhead-two">
  <svg class="trim" width="254" height="341" viewBox="0 0 254 341">
    <path d="M214 0 Q246 6 254 36 L254 0 Z" fill="var(--brown)"/>
    <path d="M0 296 Q6 334 42 341 L0 341 Z" fill="var(--brown)"/>
  </svg>
  <div class="brand">Dribblecake Bites</div>
  <div class="mascot-area" role="img" aria-label="Faint dribblecake mascot illustration"></div>
  <div class="footer tiny">Phone 0417583926 | Email Teodorblum@quillnet.com</div>
</section>

<section class="piece envelope">
  <svg class="trim" width="318" height="78" viewBox="0 0 318 78">
    <path d="M0 0 L159 44 L318 0" fill="none" stroke="var(--rule)" stroke-width="1"/>
  </svg>
  <div class="brand">Dribblecake Bites</div>
  <div class="web tiny">www.dribblecakebites.com.au</div>
</section>

<section class="piece compliments">
  <svg class="trim" width="331" height="120" viewBox="0 0 331 120">
    <path d="M0 96 Q6 116 40 120 L0 120 Z" fill="var(--brown)"/>
  </svg>
  <div class="brand">Dribblecake Bites</div>
  <div class="note strong">With Compliments</div>
  <div class="footer tiny">www.dribblecakebites.com.au</div>
</section>

</body>
</html>
```